Website refresh

We are a leading provide of JTAG hardware and software tools. We provide affordable USB and Ethernet solutions that are easily integrated into applications via a common API for Windows and Linux platforms. Our product simplicity, integration with third party applications, and free utilities have made us the provider of choice for Paragon100 companies, small businesses as well as academic and research institutions.

JTAG is an industry standard interface by which hardware and software engineers can debug, test and program their hardware or software.

Target Market(s)

We are in the technology industry, and our target audience includes hardware engineers, low level embedded software engineers, and ASIC designers.

Industry/Entity Type

Software

Requirements
Must have
• The artwork for the slider must incorporate the product photos provided.

Our new website will be a facelift for our current website (www.quillmarsh-kits.net), and must allow all the content on the current website to be incorporate into the new website (the new website may have a new CMS).
Nice to have
• Please use the screen sketches as guidance. It does not have to follow this exactly, but should allow for the various elements to be incorporated.

The design I liked is by Tomas Berenholt - his Harbor template.
http://tomasberenholt.net/templates/harbor/

here is the live demo:
http://tomasberenholt.net/files/demo/harbor/

What do you think about this? Would welcome your opinion. My product is in black plastic:
http://www.quillmarsh-kits.net/index.php?main_page=corvane

so I hope that some picture of this (to replace the photos in the templates) will work well. (I will need to include landing
pages like the one above into the new site, and there will be a few like this for other potential customers)

I would be also nice to exchange some ideas on the scrolling/rolling logos for customers (company logos) an partners (company logos)

Please let me know your thoughts.

If you are also able to do web programming, or work with someone who might be able to assist with web programming and migrating the website (while incorporating the new template), then please let me know separately.

```html
<!DOCTYPE html>
<html lang="en">
<head>
<meta charset="utf-8">
<title>Quillmarsh – JTAG cables and tools</title>
<link href="https://fonts.googleapis.com/css2?family=Ropa+Sans&family=Open+Sans:wght@400;600;700&family=Didact+Gothic&display=swap" rel="stylesheet">
<style>
:root{
  --purple:#6b2c7f;
  --ink:#1d1d1d;
  --text:#4a4a4a;
  --muted:#6a6a6a;
  --rule:#e3e3e3;
  --panel:#f1f1f1;
  --page:#ffffff;
}
*{margin:0;padding:0;box-sizing:border-box}
html,body{width:1200px;height:996px;overflow:hidden;background:var(--page)}
body{position:relative;font-family:"Open Sans",Arial,sans-serif;color:var(--text)}
a{color:inherit;text-decoration:none}
ul{list-style:none}
h1,h2,h3{font-weight:400}

.site-header{position:absolute;left:0;top:0;width:1200px;height:143px;
  background:linear-gradient(#fbfbfb,#f0f0f0);border-top:3px solid #d6d6d6}
.brand{position:absolute;left:48px;top:46px;font-family:"Open Sans",sans-serif;font-weight:700;font-size:32px;color:var(--ink);letter-spacing:-0.5px}
.brand-accent{color:var(--purple)}
.tagline{position:absolute;left:48px;top:86px;font-size:14px;font-weight:600;color:var(--ink)}
.main-nav{position:absolute;right:0;top:58px;height:64px;display:flex}
.main-nav a{display:block;padding:20px 35px 0;height:64px;font-family:"Didact Gothic",sans-serif;font-size:20px;color:#555;border-left:1px solid #dcdcdc}
.main-nav a:first-child{border-left:none}
.main-nav a:last-child{padding-right:45px}

.hero{position:absolute;left:0;top:143px;width:840px;height:377px;background:linear-gradient(#ffffff,#f2f2f2)}
.product-shot{position:absolute;left:50px;top:54px;width:325px;height:228px;border-radius:6px;
  background:linear-gradient(135deg,#efe6d8,#e1d4bf);box-shadow:0 6px 10px rgba(0,0,0,.18)}
.hero-title{position:absolute;left:404px;top:84px;font-family:"Ropa Sans",sans-serif;font-weight:400;font-size:27px;color:var(--purple)}
.hero-sub{position:absolute;left:404px;top:119px;font-family:"Ropa Sans",sans-serif;font-size:19px;color:var(--ink)}
.hero-copy{position:absolute;left:404px;top:152px;width:390px;font-size:12.5px;line-height:21px;color:var(--muted)}
.btn-learn{position:absolute;left:405px;top:273px;width:108px;height:27px;border-radius:4px;background:var(--purple);
  color:#fff;font-family:"Ropa Sans",sans-serif;font-weight:400;font-size:16px;line-height:27px;text-align:center}
.pager{position:absolute;left:741px;top:346px;display:flex;gap:2px}
.pager span{width:20px;height:20px;font-size:12px;line-height:20px;text-align:center;color:#222}
.pager .current{background:#111;color:#fff}

.news{position:absolute;left:840px;top:143px;width:360px;height:377px;background:var(--panel);
  box-shadow:inset 6px 0 8px -4px rgba(0,0,0,.12)}
.news h2{position:absolute;left:20px;top:24px;font-family:"Ropa Sans",sans-serif;font-size:27px;color:var(--purple)}
.news-item{position:absolute;left:22px;width:295px}
.news-item h3{font-size:15px;color:var(--ink);margin-bottom:2px}
.news-item p{font-size:12.5px;line-height:21px;color:var(--muted)}
.btn-more{position:absolute;left:22px;top:319px;width:110px;height:27px;border-radius:4px;background:#fff;
  font-family:"Ropa Sans",sans-serif;font-weight:400;font-size:16px;line-height:27px;padding-left:14px;color:var(--ink)}

.column{position:absolute;top:520px;height:320px}
.column h2{position:absolute;left:0;top:27px;font-family:"Ropa Sans",sans-serif;font-size:24px;color:var(--ink)}
.column .rule{position:absolute;left:0;top:62px;height:4px;background:var(--rule)}
.divider{position:absolute;top:520px;width:1px;height:320px;background:#ececec}

.quick{left:40px;width:338px}
.quick p{position:absolute;left:0;top:77px;width:305px;font-size:12.5px;line-height:20px;color:var(--ink)}
.link-list{position:absolute;top:154px;display:grid;grid-template-rows:repeat(5,28px)}
.link-list li{font-size:13.5px;color:#333}
.link-list li::before{content:"›";margin-right:10px;font-size:15px}

.partners{left:419px;width:345px}
.partner{position:absolute;font-family:"Open Sans",sans-serif;font-weight:700;font-size:26px;color:#1f3f8f}

.clients{left:804px;width:346px}
.client{position:absolute;width:102px;height:80px;border:1px solid #e2e2e2;border-radius:4px;background:#fff;
  box-shadow:0 1px 3px rgba(0,0,0,.08);font-weight:700;font-size:16px;color:#1f3f8f;text-align:center;line-height:78px}

.site-footer{position:absolute;left:0;top:876px;width:1200px;height:120px;border-top:2px solid #e6e6e6;
  background:linear-gradient(#f7f7f7,#fdfdfd)}
.copyright{position:absolute;left:34px;top:19px;font-size:13px;color:#333}
.footer-links{position:absolute;right:28px;top:19px;font-size:13.5px;color:#333}
.sep{margin:0 9px;color:#333}
</style>
</head>
<body>

<header class="site-header">
  <div class="brand">Quill<span class="brand-accent">marsh</span></div>
  <div class="tagline">JTAG cables and tools for developers and engineers</div>
  <nav class="main-nav">
    <a href="#">Product</a><a href="#">Download</a><a href="#">Support</a><a href="#">Login</a>
  </nav>
</header>

<section class="hero">
  <div class="product-shot" role="img" aria-label="Product photo of the Slingmere JTAG adapter box"></div>
  <h1 class="hero-title">Product Punch line &amp; Review</h1>
  <div class="hero-sub">tittle line goes here</div>
  <p class="hero-copy">Lanternfield eSolutions is a web service company, offering a wide range of services which range from designing and development, that is covering.<br>To be the best we know what and how to present beautifully the working of the client’s need and their advantages be highlighted.</p>
  <a class="btn-learn" href="#">learn more</a>
  <div class="pager"><span class="current">1</span><span>2</span><span>3</span><span>4</span></div>
</section>

<aside class="news">
  <h2>Latest News</h2>
  <div class="news-item" style="top:70px">
    <h3>Product Name here</h3>
    <p>To be the best we know what and how to present beautifully the working of the client’s need and their advantages be highlighted. We act in accor-dance with the Industry certified processes to deliver the best to our clients all over the world.</p>
  </div>
  <div class="news-item" style="top:216px">
    <h3>Product Name here</h3>
    <p>To be the best we know what and how to present beautifully the working of the client’s need and their advantages be highlighted.</p>
  </div>
  <a class="btn-more" href="#">View More</a>
</aside>

<section class="column quick">
  <h2>Quick links</h2><div class="rule" style="width:338px"></div>
  <p>To be the best we know what and how to present beautifully the working of the client’s need and their advantages be highlighted.</p>
  <ul class="link-list" style="left:6px">
    <li>Home</li><li>About Company</li><li>Services</li><li>Download</li><li>Support</li>
  </ul>
  <ul class="link-list" style="left:163px">
    <li>Products</li><li>Resources</li><li>News</li><li>Log In</li><li>Contact</li>
  </ul>
</section>
<div class="divider" style="left:396px"></div>

<section class="column partners">
  <h2>Our Partners</h2><div class="rule" style="width:345px"></div>
  <span class="partner" style="left:0;top:113px">Corvello</span>
  <span class="partner" style="left:163px;top:113px">Medrosa</span>
  <span class="partner" style="left:0;top:205px">Tavnor</span>
  <span class="partner" style="left:163px;top:205px">Ridgeline</span>
</section>
<div class="divider" style="left:784px"></div>

<section class="column clients">
  <h2>Our Clients &amp; Customers</h2><div class="rule" style="width:346px"></div>
  <div class="client" style="left:2px;top:89px">Fernway</div>
  <div class="client" style="left:126px;top:89px">Lumio</div>
  <div class="client" style="left:246px;top:89px">Kestal</div>
  <div class="client" style="left:2px;top:189px">Orvin</div>
  <div class="client" style="left:126px;top:189px">Pallis</div>
  <div class="client" style="left:246px;top:189px">Tarrow</div>
</section>

<footer class="site-footer">
  <div class="copyright">Copyright © 2012 Company Name <span class="sep">|</span>Term &amp; Conditions</div>
  <div class="footer-links">Policy<span class="sep">|</span>Developers<span class="sep">|</span>About Us<span class="sep">|</span>Contact Us</div>
</footer>

</body>
</html>
```